Offshore Energy Projects Management Consultancy needs a business card design

Logo available. We provide teams to deliver engineering consultancy, project management and delivery teams mainly in the offshore renewables sector. The company is all about bringing the right people to a project to deliver the scope.

The business card will be used for all staff.

The business card should be quite simple, vibrant and uncluttered but convey experience, enthusiasm and integration.

Target Market(s)

Energy Project Developers and Tier 1 construction companies

Contact Information for Business Card

Logo should be on the back of the card. I'm happy for the designer to play with the colour of the logo and background colour.

Front of the card should convey all the must have information in a clear and professional manner but without being overly traditional.

Colors

Designer to choose colors to be used in the design.

Requirements
Must have
• Land Line Tel Number, Mobile Tel Number, Email, business address, web address.

```html
<!DOCTYPE html>
<html lang="en">
<head>
<meta charset="utf-8">
<title>Seaward Works Group – Business Cards</title>
<link href="https://fonts.googleapis.com/css2?family=Montserrat:wght@400;500;700&display=swap" rel="stylesheet">
<style>
:root{
  --stage:#6d6e70;
  --white:#ffffff;
  --blue-deep:#0a6fc0;
  --blue-mid:#1a6fb8;
  --blue-light:#29a6e0;
  --grey-text:#636466;
  --ghost:#e6e6e6;
}
*{margin:0;padding:0;box-sizing:border-box}
html,body{width:1200px;height:1200px;overflow:hidden;background:var(--stage);font-family:'Montserrat',sans-serif}
.card{position:absolute;left:305px;width:590px;height:360px;background:var(--white);overflow:hidden}
.card--front{top:16px}
.card--back{top:389px}
.card--alt{top:759px}

/* front card */
.brand-panel{position:absolute;left:0;top:0;width:229px;height:100%;display:flex;align-items:center;justify-content:center}
.wordmark{color:var(--grey-text);font-weight:700;text-align:center;letter-spacing:.5px;line-height:1.15;position:relative;z-index:1}
.brand-panel .wordmark{font-size:17px}
.info-panel{position:absolute;left:229px;top:0;right:0;bottom:0;background:linear-gradient(180deg,var(--blue-deep),var(--blue-light));color:var(--white);padding:0 12px}
.headline{font-size:27px;font-weight:400;white-space:nowrap;position:relative;z-index:1}
.headline strong{font-weight:700}
.info-panel .headline{margin-top:27px}
.info-panel .tagline{font-size:8.6px;line-height:1.35;margin-top:8px;width:320px}
.contact-list{list-style:none;position:absolute;left:12px;top:124px}
.contact-list li{display:flex;align-items:center;height:46px;margin-bottom:13px;font-size:14.5px}
.tile{width:46px;height:46px;border-radius:7px;display:flex;align-items:center;justify-content:center;flex:none}
.tile svg{width:30px;height:30px}
.tile--light{background:var(--white);color:var(--blue-mid)}
.tile--solid{background:linear-gradient(135deg,var(--blue-light),var(--blue-deep));color:var(--white)}
.contact-list .label{margin-left:12px;line-height:1.05}

/* faint name decoration */
.ghost-name{position:absolute;left:0;right:0;text-align:center;color:var(--ghost);font-weight:700;white-space:nowrap;line-height:1;z-index:0}

/* back card */
.card--back .wordmark{position:absolute;left:0;right:0;top:170px;font-size:30px}
.card--back .ghost-name{top:222px;font-size:40px}

/* alt card */
.card--alt .headline{position:absolute;left:0;right:0;top:80px;text-align:center;color:var(--blue-mid);font-size:29px}
.card--alt .tagline{position:absolute;left:60px;right:60px;top:137px;text-align:center;color:var(--blue-light);font-size:14px;line-height:1.2;z-index:1}
.card--alt .ghost-name{top:193px;font-size:36px}
.contact-row{position:absolute;top:228px;left:0;right:0;height:46px;z-index:1}
.contact-row .item{position:absolute;display:flex;align-items:center;color:var(--blue-mid);font-weight:700;font-size:14px}
.contact-row .item .label{margin-left:8px}
.address-band{position:absolute;left:0;right:0;bottom:0;height:72px;background:linear-gradient(90deg,var(--blue-light),var(--blue-deep));display:flex;align-items:center;padding-left:135px;color:var(--white);font-weight:700;font-size:14px;line-height:1.05;z-index:1}
.address-band .label{margin-left:12px}
</style>
</head>
<body>
<svg width="0" height="0" style="position:absolute" aria-hidden="true">
  <defs>
    <symbol id="i-phone" viewBox="0 0 32 32" fill="none" stroke="currentColor" stroke-width="1.6" stroke-linecap="round" stroke-linejoin="round">
      <path d="M9 5l4 5-2.5 2.5c1.5 3.5 4 6 7.5 7.5L20.5 17.5l5 4-2.5 4C14 25 7 18 6 8.5z"/>
      <path d="M18 5a9 9 0 0 1 9 9M18 9a5 5 0 0 1 5 5"/>
    </symbol>
    <symbol id="i-mail" viewBox="0 0 32 32" fill="none" stroke="currentColor" stroke-width="1.6" stroke-linejoin="round">
      <rect x="4" y="8" width="24" height="16" rx="1.5"/><path d="M4 9l12 9 12-9"/>
    </symbol>
    <symbol id="i-globe" viewBox="0 0 32 32" fill="none" stroke="currentColor" stroke-width="1.5">
      <circle cx="16" cy="16" r="12"/><ellipse cx="16" cy="16" rx="5.5" ry="12"/><path d="M4 16h24M6 10h20M6 22h20M16 4v24"/>
    </symbol>
    <symbol id="i-pin" viewBox="0 0 32 32" fill="none" stroke="currentColor" stroke-width="1.6" stroke-linejoin="round">
      <path d="M16 29s-9-9.5-9-16a9 9 0 0 1 18 0c0 6.5-9 16-9 16z"/><circle cx="16" cy="13" r="4"/>
    </symbol>
  </defs>
</svg>

<section class="card card--front">
  <div class="brand-panel"><p class="wordmark">SEAWARD WORKS<br>GROUP</p></div>
  <div class="info-panel">
    <h1 class="headline"><strong>Worldwide</strong> Consultancy</h1>
    <p class="tagline">Dedicated to ensure that we provide the right advise and solution as part of our service, we focus on providing quality and don't focus on the quantity.</p>
    <ul class="contact-list">
      <li><span class="tile tile--light"><svg><use href="#i-phone"/></svg></span><span class="label">+44 1632 960 330</span></li>
      <li><span class="tile tile--light"><svg><use href="#i-mail"/></svg></span><span class="label">info@swg.ltd</span></li>
      <li><span class="tile tile--light"><svg><use href="#i-globe"/></svg></span><span class="label">www.swg.ltd</span></li>
      <li><span class="tile tile--light"><svg><use href="#i-pin"/></svg></span><span class="label">The Harbour Building,<br>12 Quay Road, Portmere, PM1 4QA</span></li>
    </ul>
  </div>
</section>

<section class="card card--back">
  <p class="wordmark">SEAWARD WORKS GROUP</p>
  <p class="ghost-name" aria-hidden="true">SEAWARD WORKS GROUP</p>
</section>

<section class="card card--alt">
  <h2 class="headline"><strong>Worldwide</strong> Consultancy</h2>
  <p class="tagline">Dedicated to ensure that we provide the right advise and solution as part of our service, we focus on providing quality and don't focus on the quantity.</p>
  <p class="ghost-name" aria-hidden="true">SEAWARD WORKS GROUP</p>
  <div class="contact-row">
    <div class="item" style="left:13px"><span class="tile tile--solid"><svg><use href="#i-phone"/></svg></span><span class="label">+44 1632 960 330</span></div>
    <div class="item" style="left:238px"><span class="tile tile--solid"><svg><use href="#i-mail"/></svg></span><span class="label">info@swg.ltd</span></div>
    <div class="item" style="left:433px"><span class="tile tile--solid"><svg><use href="#i-globe"/></svg></span><span class="label">www.swg.ltd</span></div>
  </div>
  <div class="address-band">
    <span class="tile tile--light"><svg><use href="#i-pin"/></svg></span>
    <span class="label">The Harbour Building,<br>12 Quay Road, Portmere, PM1 4QA</span>
  </div>
</section>
</body>
</html>
```